Voltwise - Flyer design

Description -
Motorhome and Caravan EWOFs
Recreational Vehicles (such as caravans, motorhomes, RVs, Boats etc) and Relocatable buildings that can be connected to an electricity supply must be regularly checked for electrical safety. An EWOF needs to be issued every 4 years.
Pre-purchase house inspections
A pre-purchase electrical inspection prior to buying a home can be used to identify any dangerous and unsafe electrical parts of the installation that may be costly to repair once the property has been purchased. Giving you peace of mind when buying your new home.
High risk Electrical inspections
All Prescribed Electrical Work that falls under the High Risk category must be inspected by a Registered Electrical Inspector and have a Record of Inspection certificate issued.
Electric Vehicle Chargers
Any electrical vehicle charger that can be accessed by the public (ie in a non-domestic situation) must be periodically inspected and certified every 12 months.
General Electrical Services
Domestic and commercial - We do new builds, Renovations, Maintenance and more!
Dean Porter - Electrician and Electrical Inspector
Ph - 0275381942
Dean@voltwise-sample.co.nz
Auckland
------
I also want there to be a few symbols similar to the files I have attached.
The main areas that I am hoping to find work is with caravans/motohomes and EV car chargers so these symbols are quite important.
Thanks so much

```html
<!DOCTYPE html>
<html lang="en">
<head>
<meta charset="utf-8">
<title>Voltwise – Our Services Flyer</title>
<link href="https://fonts.googleapis.com/css2?family=Black+Ops+One&family=Nunito:wght@700;800&display=swap" rel="stylesheet">
<style>
  :root {
    --green: #8cc63f;
    --grey: #5e5e5e;
    --ink: #111111;
    --paper: #ffffff;
    --backdrop: #ededed;
  }
  * { margin: 0; padding: 0; box-sizing: border-box; }
  html, body { width: 1200px; height: 1200px; overflow: hidden; background: var(--backdrop); }
  .flyer {
    position: absolute; left: 190px; top: 20px;
    width: 820px; height: 1160px;
    background: var(--paper); overflow: hidden;
    font-family: "Nunito", Arial, sans-serif;
  }
  .brand { position: absolute; left: 16px; top: 17px; display: flex; align-items: center; gap: 10px; }
  .brand-mark { width: 30px; height: 30px; border: 4px solid var(--green); }
  .brand-name { font-family: "Nunito", Arial, sans-serif; font-weight: 800; font-size: 34px; color: var(--grey); }
  .title {
    position: absolute; left: 172px; top: 108px;
    font-family: "Black Ops One", Impact, sans-serif;
    font-size: 64px; color: var(--grey); letter-spacing: 1px; white-space: nowrap;
  }
  .service { position: absolute; }
  .service h2 {
    font-family: "Black Ops One", Impact, sans-serif; font-weight: 400;
    font-size: 20px; color: #333; margin-bottom: 6px; white-space: nowrap;
  }
  .service p { font-weight: 800; font-size: 13px; line-height: 16.5px; color: var(--ink); }
  .icon { position: absolute; fill: none; stroke: #222; stroke-width: 2; stroke-linejoin: round; stroke-linecap: round; }
  .photo {
    position: absolute; left: 18px; top: 580px; width: 544px; height: 268px;
    border: 3px solid var(--ink); border-radius: 14px;
    background: linear-gradient(110deg, #4a4a52 0%, #9d8c7c 40%, #c99779 70%, #2b2725 100%);
  }
  .pattern { position: absolute; background: linear-gradient(135deg, var(--green), #a9a9a9 55%, var(--grey)); opacity: .55; }
  .contact { position: absolute; left: 279px; top: 930px; }
  .contact h3 { font-family: "Black Ops One", Impact, sans-serif; font-weight: 400; font-size: 27px; color: var(--green); margin-bottom: 4px; }
  .contact p { font-weight: 800; font-size: 19px; line-height: 24.8px; color: var(--ink); }
  .social { position: absolute; left: 274px; top: 1089px; display: flex; gap: 10px; }
  .social span { width: 46px; height: 46px; border-radius: 50%; background: var(--green); display: flex; align-items: center; justify-content: center; }
</style>
</head>
<body>
<main class="flyer">
  <div class="brand"><span class="brand-mark"></span><span class="brand-name">Voltwise</span></div>

  <div class="pattern" style="left:648px;top:0;width:172px;height:161px" role="img" aria-label="Decorative cluster of green and grey squares"></div>
  <div class="pattern" style="left:714px;top:360px;width:106px;height:100px" role="img" aria-label="Decorative green and grey squares"></div>
  <div class="pattern" style="left:586px;top:500px;width:234px;height:660px" role="img" aria-label="Decorative column of green and grey squares"></div>
  <div class="pattern" style="left:0;top:862px;width:216px;height:298px" role="img" aria-label="Decorative cluster of green and grey squares"></div>

  <h1 class="title">Our Services</h1>

  <svg class="icon" style="left:44px;top:244px" width="62" height="34" viewBox="0 0 62 34">
    <rect x="8" y="3" width="52" height="24" rx="5"/>
    <rect x="14" y="8" width="14" height="7"/><rect x="42" y="8" width="9" height="15"/>
    <circle cx="36" cy="28" r="4"/><path d="M8 24H1v4"/>
  </svg>
  <section class="service" style="left:113px;top:218px;width:270px">
    <h2>Motorhome and Caravan EWOFs</h2>
    <p>Recreational Vehicles (such as caravans, motorhomes, RVs, Boats etc) and Relocatable buildings that can be connected to an electricity supply must be regularly checked for electrical safety. An EWOF needs to be issued every 4 years.</p>
  </section>

  <svg class="icon" style="left:426px;top:241px" width="48" height="48" viewBox="0 0 48 48">
    <path d="M3 24L24 3l21 21M8 19v27h32V19"/><path d="M26 16l-7 12h6l-3 10 8-13h-6z"/>
  </svg>
  <section class="service" style="left:483px;top:218px;width:300px">
    <h2>Pre-Purchase House</h2>
    <p>A pre-purchase electrical inspection prior to buying a home can be used to identify any dangerous and unsafe electrical parts of the installation that may be costly to repair once the property has been purchased. Giving you peace of mind when buying your new home.</p>
  </section>

  <svg class="icon" style="left:60px;top:388px" width="44" height="40" viewBox="0 0 44 40">
    <path d="M22 2L42 38H2z"/><path d="M24 13l-6 12h5l-3 9 8-13h-5z"/>
  </svg>
  <section class="service" style="left:113px;top:364px;width:270px">
    <h2>High Risk Electrical</h2>
    <p>All Prescribed Electrical Work that falls under the High Risk category must be inspected by a Registered Electrical Inspector and have a Record of Inspection certificate issued.</p>
  </section>

  <svg class="icon" style="left:441px;top:388px" width="38" height="46" viewBox="0 0 38 46">
    <rect x="3" y="2" width="24" height="38" rx="3"/><rect x="7" y="6" width="16" height="9"/>
    <path d="M16 19l-5 9h4l-2 7 6-10h-4z"/><path d="M1 44h28M27 12h5v18a3 3 0 0 0 3-3V8"/>
  </svg>
  <section class="service" style="left:485px;top:364px;width:218px">
    <h2>Electric Vehicle</h2>
    <p>Any electrical vehicle charger that can be accessed by the public (ie in a non-domestic situation) must be periodically inspected and certified every 12 months.</p>
  </section>

  <svg class="icon" style="left:261px;top:502px" width="38" height="52" viewBox="0 0 38 52">
    <path d="M26 1L3 30h14L10 51 35 20H21z"/>
  </svg>
  <section class="service" style="left:308px;top:488px;width:240px">
    <h2>General Electrical</h2>
    <p>Domestic and commercial - We do new builds, Renovations, Maintenance and more!</p>
  </section>

  <div class="photo" role="img" aria-label="Photo of an electrician testing a vehicle with a handheld meter"></div>

  <section class="contact">
    <h3>Contact Us</h3>
    <p>Dean Porter - Electrician and<br>Electrical Inspector<br>Ph - 0275381942<br>Dean@voltwise-sample.co.nz<br>Auckland</p>
  </section>

  <div class="social">
    <span aria-label="Social link"></span>
    <span aria-label="Email">
      <svg width="28" height="20" viewBox="0 0 28 20" fill="none" stroke="#fff" stroke-width="2"><rect x="1" y="1" width="26" height="18" rx="2"/><path d="M1 2l13 10L27 2"/></svg>
    </span>
    <span aria-label="Social link"></span>
    <span aria-label="Social link"></span>
  </div>
</main>
</body>
</html>
```